Candy jar labels

design three candy jar labels in similar vein to our current glass jar range Hale Kin. SWEETS.
The flavours are: Creamy Soda, Bananas & Cream, Polar Frost Drops.
Creamy Soda - art deco style, light and dark pinks
Bananas & Cream - 60/70's style
Polar Frost Drops - blue with white snowflakes
Uploaded labels are for ideas I like in the past, but not to be the same. Also look at our website to see the different designs we have, but I would like some funky new looking ones for these new flavours.
Once the artwork is correct then there is specific data I will need added each side, which I will provide later on a spreadsheet.
Like Apple Rock and Velvet Wee Bits - the bottom and top banner must be outlined.
This files given to me at the end need to be editable on the text since in the future I will need to manually update myself the batch and lot number for each order.

```html
<!DOCTYPE html>
<html lang="en">
<head>
<meta charset="utf-8">
<title>Hale Kin. SWEETS – Candy Jar Labels</title>
<link rel="stylesheet" href="https://fonts.googleapis.com/css2?family=Roboto:wght@400;500;700&family=Roboto+Slab:wght@500;600&family=Fredoka:wght@700&family=Titan+One&family=Oswald:wght@700&display=swap">
<style>
  :root {
    --page-white: #ffffff;
    --soda-page: #fdeef5;
    --banana-page: #fdf6dc;
    --mint-page: #eff6fb;

    --soda-bg: #f6b1d6;
    --soda-ink: #97186f;
    --soda-light: #f7bcdc;
    --soda-accent: #e06aa8;

    --banana-bg: #ecc21b;
    --banana-ink: #1d6b99;
    --banana-art-a: #a9c6e6;
    --banana-art-b: #6e9ccf;

    --mint-bg: #1c6a96;
    --mint-ink: #ffffff;
    --mint-light: #cde9f8;
    --mint-accent: #1c98d8;
    --mint-deep: #125a85;
  }
  * { box-sizing: border-box; margin: 0; padding: 0; }
  html, body { width: 800px; height: 1200px; overflow: hidden; }
  body {
    position: relative;
    background: var(--page-white);
    font-family: "Roboto", Arial, sans-serif;
  }

  .band { position: absolute; left: 71px; width: 729px; }
  .band--soda { top: 0; height: 400px; background: var(--soda-page); }
  .band--banana { top: 400px; height: 400px; background: var(--banana-page); }
  .band--mint { top: 800px; height: 400px; background: var(--mint-page); }

  .label {
    position: absolute;
    left: 117px;
    width: 611px;
    height: 290px;
    background: var(--label-bg);
    color: var(--ink);
    box-shadow: 0 16px 14px -10px rgba(0,0,0,.35);
    overflow: hidden;
  }
  .label--soda { top: 43px; --label-bg: var(--soda-bg); --ink: var(--soda-ink); }
  .label--banana { top: 443px; --label-bg: var(--banana-bg); --ink: var(--banana-ink); }
  .label--mint { top: 844px; --label-bg: var(--mint-bg); --ink: var(--mint-ink); }

  .label-art { position: absolute; inset: 0; width: 611px; height: 290px; }

  /* left information panel */
  .info { position: absolute; left: 12px; top: 13px; width: 125px; font-size: 6.3px; line-height: 1.25; }
  .info-title { font-size: 8px; line-height: 1.25; }
  .info-title b, .info-heading { font-weight: 700; }
  .info-heading { font-size: 8px; margin-top: 6px; }
  .info-serving { font-size: 6.6px; line-height: 1.2; }
  .nutrition { width: 123px; border-collapse: collapse; margin-top: 2px; font-size: 6.4px; }
  .nutrition thead th { font-weight: 400; font-size: 3.8px; line-height: 1.05; text-align: center; padding: 2px 0 4px; border-top: .6px solid currentColor; border-bottom: .6px solid currentColor; }
  .nutrition td { padding: 0; line-height: 8.2px; }
  .nutrition td:nth-child(2), .nutrition td:nth-child(3) { text-align: right; padding-right: 4px; }
  .nutrition .gap td { height: 8px; }
  .nutrition tbody tr:last-child td { border-bottom: .6px solid currentColor; padding-bottom: 2px; }
  .info-block { margin-top: 5px; font-size: 6.2px; line-height: 1.3; }
  .info-block b { font-weight: 700; }
  .info-small { font-size: 5.2px; line-height: 1.3; }
  .info-tags { margin-top: 3px; font-size: 6px; font-weight: 700; display: flex; gap: 3px; align-items: center; }
  .info-tags span.tag-box { border: .6px solid currentColor; padding: 0 2px; font-size: 5.2px; }
  .owned {
    position: absolute; left: 23px; top: 259px; width: 100px; height: 14px;
    border: 1px solid var(--ink); border-radius: 3px;
    font-size: 8.2px; font-weight: 500; text-align: center; line-height: 12px;
  }
  .label--soda .owned { background: var(--soda-ink); color: var(--soda-light); border-color: #fff; }
  .label--banana .owned { background: var(--banana-ink); color: var(--banana-bg); border-color: #fff; }
  .label--mint .owned { color: #fff; border-color: #fff; }

  /* gluten free badge */
  .badge {
    position: absolute; left: 282px; top: 21px; width: 136px; height: 34px;
    border-radius: 7px; text-align: center;
    font-family: "Roboto Slab", Georgia, serif; font-weight: 600; font-size: 17px; letter-spacing: .3px;
    line-height: 22px; padding-top: 2px;
  }
  .badge-dots { display: flex; justify-content: center; align-items: center; gap: 4px; margin-top: -2px; }
  .badge-dots i { display: block; width: 3px; height: 3px; border-radius: 50%; background: currentColor; }
  .badge-dots i.big { width: 6px; height: 6px; }
  .label--soda .badge { background: var(--soda-light); color: var(--soda-ink); border: 3px solid var(--soda-ink); }
  .label--banana .badge { background: var(--banana-ink); color: #fff; border: 3px solid var(--banana-ink); box-shadow: inset 0 0 0 1.5px #fff; }
  .label--mint .badge { background: var(--mint-light); color: var(--mint-deep); border: 3px solid var(--mint-accent); }

  /* bottom banner */
  .banner {
    position: absolute; left: 173px; top: 232px; width: 216px; height: 40px;
    border-radius: 8px; text-align: center;
    font-family: "Roboto Slab", Georgia, serif; font-weight: 500;
  }
  .banner-net { font-size: 12.5px; line-height: 15px; margin-top: 2px; display: flex; justify-content: center; align-items: center; gap: 3px; }
  .banner-net i { display: block; width: 3px; height: 3px; border-radius: 50%; background: currentColor; }
  .banner-net i.mid { width: 4px; height: 4px; }
  .banner-net i.big { width: 6px; height: 6px; }
  .banner-net span { margin: 0 3px; }
  .banner-tag { font-size: 15px; line-height: 18px; letter-spacing: -.2px; }
  .label--soda .banner { background: var(--soda-light); color: var(--soda-ink); border: 3px solid var(--soda-ink); }
  .label--banana .banner { background: var(--banana-ink); color: #fff; border: 3px solid var(--banana-ink); box-shadow: inset 0 0 0 1.5px #fff; }
  .label--mint .banner { background: var(--mint-light); color: var(--mint-deep); border: 3px solid var(--mint-accent); }

  /* product titles */
  .brand-name { font-family: "Roboto", Arial, sans-serif; font-weight: 400; display: block; }

  .title-soda {
    position: absolute; left: 200px; top: 76px; width: 236px; height: 128px;
    background: #fff; border: 5px solid var(--soda-bg); border-radius: 10px;
    box-shadow: 0 0 0 2px var(--soda-ink), inset 0 0 0 2px var(--soda-ink);
    transform: rotate(-6deg); text-align: center; color: var(--soda-ink);
  }
  .title-soda .brand-name { color: var(--soda-accent); font-size: 17px; margin-top: 10px; }
  .title-soda .product-name { font-family: "Fredoka", Arial, sans-serif; font-weight: 700; font-size: 40px; line-height: 38px; letter-spacing: .5px; }

  .title-banana {
    position: absolute; left: 201px; top: 86px; width: 230px; height: 120px;
    background: #fff; border: 6px solid var(--banana-bg); border-radius: 14px;
    box-shadow: 0 0 0 2px var(--banana-ink), inset 0 0 0 2px var(--banana-ink);
    text-align: center; color: var(--banana-ink);
  }
  .title-banana .brand-name { font-size: 16px; margin-top: 8px; }
  .title-banana .product-name { font-family: "Titan One", Arial, sans-serif; font-size: 34px; line-height: 34px; margin-top: 2px; }

  .title-mint {
    position: absolute; left: 236px; top: 64px; width: 156px; height: 156px; border-radius: 50%;
    background: var(--mint-accent); border: 3px solid var(--mint-light);
    text-align: center; color: var(--mint-light);
  }
  .title-mint .brand-name { font-size: 17px; margin-top: 22px; color: #fff; }
  .title-mint .product-name {
    position: absolute; left: -30px; right: -30px; top: 44px;
    font-family: "Oswald", Arial, sans-serif; font-weight: 700; font-size: 31px; line-height: 34px;
    color: var(--mint-light); -webkit-text-stroke: 2px var(--mint-deep); paint-order: stroke fill;
    letter-spacing: -.3px;
  }

  /* right contact panel */
  .contact { position: absolute; left: 476px; top: 125px; width: 134px; text-align: center; font-size: 7px; line-height: 8.7px; }
  .contact-brand { font-size: 8.5px; font-weight: 500; line-height: 12px; margin-bottom: 1px; }
  .contact-web { margin-top: 2.5px; }
  .contact-social { display: flex; justify-content: center; align-items: center; gap: 2px; margin-top: 1px; }
  .contact-social i { display: block; width: 6px; height: 6px; border-radius: 50%; background: currentColor; }
  .batch {
    position: absolute; left: 486px; top: 250px; width: 114px; height: 19px;
    border: 1px solid var(--ink); text-align: center; font-size: 5.4px; line-height: 7.5px; padding-top: 1px;
  }
  .batch b { font-weight: 700; }
</style>
</head>
<body>
  <div class="band band--soda"></div>
  <div class="band band--banana"></div>
  <div class="band band--mint"></div>

  <!-- Creamy Soda -->
  <section class="label label--soda">
    <svg class="label-art" viewBox="0 0 611 290">
      <defs>
        <linearGradient id="soda-art" x1="0" y1="0" x2="0" y2="1">
          <stop offset="0" stop-color="#6e1150"/>
          <stop offset=".5" stop-color="#a8457f"/>
          <stop offset="1" stop-color="#6e1150"/>
        </linearGradient>
      </defs>
      <path role="img" aria-label="Art deco horizontal stripe pattern in dark and light pinks" d="M209,0 C165,80 138,170 150,290 L449,290 C478,180 480,80 459,0 Z" fill="url(#soda-art)"/>
      <path d="M209,0 C165,80 138,170 150,290 M449,290 C478,180 480,80 459,0" fill="none" stroke="var(--soda-ink)" stroke-width="7"/>
    </svg>
    <div class="info">
      <p class="info-title"><b>Apple Rock -</b> green apple flavoured confectionery.</p>
      <p class="info-heading">Nutrition Information</p>
      <p class="info-serving">Serving per package: 8.75<br>Serving size: 20 g (approx. 3 lollies )</p>
      <table class="nutrition">
        <thead><tr><th></th><th>Average<br>Qty. Per<br>Serving</th><th>Average<br>Qty. Per<br>100g</th></tr></thead>
        <tbody>
          <tr><td>Energy</td><td>195 kJ</td><td>975 kJ</td></tr>
          <tr><td></td><td>(47 cal)</td><td>(235 cal)</td></tr>
          <tr><td>Protein</td><td>0 g</td><td>0 g</td></tr>
          <tr><td>Fat, total</td><td>&lt; 1 g</td><td>&lt; 1 g</td></tr>
          <tr><td>-saturated</td><td>&lt; 1 g</td><td>&lt; 1 g</td></tr>
          <tr><td>Carbohydrate</td><td>11.4 g</td><td>57 g</td></tr>
          <tr><td>-sugars</td><td>10.7 g</td><td>53.5 g</td></tr>
          <tr><td>Sodium</td><td>5 mg</td><td>23 mg</td></tr>
        </tbody>
      </table>
      <p class="info-block"><b>INGREDIENTS:</b> WHITE SUGAR, GLUCOSE SYRUP (CORN), WATER, CITRIC ACID (330), FLAVOUR, COLOURS (102, 129, 133).</p>
      <p class="info-small"><b>ALLERGEN STATEMENT:</b> Produced in a factory that does not use nuts, tree nuts, or gluten.</p>
      <p class="info-tags">GLUTEN FREE <span class="tag-box">Product of China</span></p>
      <p class="info-small" style="margin-top:3px">Product sold by weight not by volume. Contents tend to settle after packaging. <b>Directions for use:</b> Best consumed within 7 days of opening. <b>Storage conditions:</b> Store in cool dry conditions. Do not refrigerate. May go sticky after exposure to air.</p>
    </div>
    <div class="owned">AUSTRALIAN OWNED</div>
    <div class="badge">GLUTEN FREE<div class="badge-dots"><i></i><i></i><i></i><i class="big"></i><i></i><i></i><i></i></div></div>
    <div class="title-soda"><span class="brand-name">Hale Kin.</span><div class="product-name">CREAMY<br>SODA</div></div>
    <div class="banner"><div class="banner-net"><i></i><i class="mid"></i><i class="big"></i><span>175g NET</span><i class="big"></i><i class="mid"></i><i></i></div><div class="banner-tag">A flavour for every memory!</div></div>
    <div class="contact">
      <p class="contact-brand">Hale Kin. SWEETS</p>
      <p>88 Harbour Lane<br>Level 2, Suite 410<br>CAIRNS QLD 4870<br>PO Box 19<br>KURANDA QLD 4881<br>AUSTRALIA<br>+61 (07) 4000 1234</p>
      <p class="contact-web">www.halekinsweets.com<br>AU: sales@halekinsweets.com.au<br>USA, EU, UK, Canada:<br>sales@halekinsweets.com</p>
      <p class="contact-social"><i></i>HaleKinSweets</p>
    </div>
    <div class="batch"><b>Best before:</b> Jun 2028<br><b>Batch/lot number:</b> 1400/09001-26007</div>
  </section>

  <!-- Bananas & Cream -->
  <section class="label label--banana">
    <svg class="label-art" viewBox="0 0 611 290">
      <defs>
        <linearGradient id="banana-art" x1="0" y1="0" x2="1" y2="1">
          <stop offset="0" stop-color="var(--banana-art-a)"/>
          <stop offset="1" stop-color="var(--banana-art-b)"/>
        </linearGradient>
      </defs>
      <path role="img" aria-label="Retro 60s/70s pattern of yellow bananas and blue leaves" d="M209,0 C165,80 138,170 150,290 L449,290 C478,180 480,80 459,0 Z" fill="url(#banana-art)"/>
      <path d="M209,0 C165,80 138,170 150,290 M449,290 C478,180 480,80 459,0" fill="none" stroke="var(--banana-ink)" stroke-width="5"/>
    </svg>
    <div class="info">
      <p class="info-title"><b>Apple Rock -</b> green apple flavoured confectionery.</p>
      <p class="info-heading">Nutrition Information</p>
      <p class="info-serving">Serving per package: 8.75<br>Serving size: 20 g (approx. 3 lollies )</p>
      <table class="nutrition">
        <thead><tr><th></th><th>Average<br>Qty. Per<br>Serving</th><th>Average<br>Qty. Per<br>100g</th></tr></thead>
        <tbody>
          <tr><td>Energy</td><td>195 kJ</td><td>975 kJ</td></tr>
          <tr><td></td><td>(47 cal)</td><td>(235 cal)</td></tr>
          <tr><td>Protein</td><td>0 g</td><td>0 g</td></tr>
          <tr><td>Fat, total</td><td>&lt; 1 g</td><td>&lt; 1 g</td></tr>
          <tr><td>-saturated</td><td>&lt; 1 g</td><td>&lt; 1 g</td></tr>
          <tr><td>Carbohydrate</td><td>11.4 g</td><td>57 g</td></tr>
          <tr><td>-sugars</td><td>10.7 g</td><td>53.5 g</td></tr>
          <tr><td>Sodium</td><td>5 mg</td><td>23 mg</td></tr>
        </tbody>
      </table>
      <p class="info-block"><b>INGREDIENTS:</b> WHITE SUGAR, GLUCOSE SYRUP (CORN), WATER, CITRIC ACID (330), FLAVOUR, COLOURS (102, 129, 133).</p>
      <p class="info-small"><b>ALLERGEN STATEMENT:</b> Produced in a factory that does not use nuts, tree nuts, or gluten.</p>
      <p class="info-tags">GLUTEN FREE <span class="tag-box">Product of China</span></p>
      <p class="info-small" style="margin-top:3px">Product sold by weight not by volume. Contents tend to settle after packaging. <b>Directions for use:</b> Best consumed within 7 days of opening. <b>Storage conditions:</b> Store in cool dry conditions. Do not refrigerate. May go sticky after exposure to air.</p>
    </div>
    <div class="owned">AUSTRALIAN OWNED</div>
    <div class="badge">GLUTEN FREE<div class="badge-dots"><i></i><i></i><i></i><i class="big"></i><i></i><i></i><i></i></div></div>
    <div class="title-banana"><span class="brand-name">Hale Kin.</span><div class="product-name">Bananas<br>&amp; Cream</div></div>
    <div class="banner"><div class="banner-net"><i></i><i class="mid"></i><i class="big"></i><span>175g NET</span><i class="big"></i><i class="mid"></i><i></i></div><div class="banner-tag">A flavour for every memory!</div></div>
    <div class="contact">
      <p class="contact-brand">Hale Kin. SWEETS</p>
      <p>88 Harbour Lane<br>Level 2, Suite 410<br>CAIRNS QLD 4870<br>PO Box 19<br>KURANDA QLD 4881<br>AUSTRALIA<br>+61 (07) 4000 1234</p>
      <p class="contact-web">www.halekinsweets.com<br>AU: sales@halekinsweets.com.au<br>USA, EU, UK, Canada:<br>sales@halekinsweets.com</p>
      <p class="contact-social"><i></i>HaleKinSweets</p>
    </div>
    <div class="batch"><b>Best before:</b> Jun 2028<br><b>Batch/lot number:</b> 1400/09001-26007</div>
  </section>

  <!-- Polar Frost Drops -->
  <section class="label label--mint">
    <svg class="label-art" viewBox="0 0 611 290">
      <defs>
        <radialGradient id="mint-art" cx=".5" cy=".5" r=".6">
          <stop offset="0" stop-color="#ffffff"/>
          <stop offset="1" stop-color="#a9d7f3"/>
        </radialGradient>
      </defs>
      <path role="img" aria-label="Icy light blue background scattered with white snowflakes" d="M209,0 C165,80 138,170 150,290 L449,290 C478,180 480,80 459,0 Z" fill="url(#mint-art)"/>
      <path d="M209,0 C165,80 138,170 150,290 M449,290 C478,180 480,80 459,0" fill="none" stroke="var(--mint-accent)" stroke-width="5"/>
    </svg>
    <div class="info">
      <p class="info-title"><b>Apple Rock -</b> green apple flavoured confectionery.</p>
      <p class="info-heading">Nutrition Information</p>
      <p class="info-serving">Serving per package: 8.75<br>Serving size: 20 g (approx. 3 lollies )</p>
      <table class="nutrition">
        <thead><tr><th></th><th>Average<br>Qty. Per<br>Serving</th><th>Average<br>Qty. Per<br>100g</th></tr></thead>
        <tbody>
          <tr><td>Energy</td><td>195 kJ</td><td>975 kJ</td></tr>
          <tr><td></td><td>(47 cal)</td><td>(235 cal)</td></tr>
          <tr><td>Protein</td><td>0 g</td><td>0 g</td></tr>
          <tr><td>Fat, total</td><td>&lt; 1 g</td><td>&lt; 1 g</td></tr>
          <tr><td>-saturated</td><td>&lt; 1 g</td><td>&lt; 1 g</td></tr>
          <tr><td>Carbohydrate</td><td>11.4 g</td><td>57 g</td></tr>
          <tr><td>-sugars</td><td>10.7 g</td><td>53.5 g</td></tr>
          <tr><td>Sodium</td><td>5 mg</td><td>23 mg</td></tr>
        </tbody>
      </table>
      <p class="info-block"><b>INGREDIENTS:</b> WHITE SUGAR, GLUCOSE SYRUP (CORN), WATER, CITRIC ACID (330), FLAVOUR, COLOURS (102, 129, 133).</p>
      <p class="info-small"><b>ALLERGEN STATEMENT:</b> Produced in a factory that does not use nuts, tree nuts, or gluten.</p>
      <p class="info-tags">GLUTEN FREE <span class="tag-box">Product of China</span></p>
      <p class="info-small" style="margin-top:3px">Product sold by weight not by volume. Contents tend to settle after packaging. <b>Directions for use:</b> Best consumed within 7 days of opening. <b>Storage conditions:</b> Store in cool dry conditions. Do not</p>
    </div>
    <div class="owned">AUSTRALIAN OWNED</div>
    <div class="badge">GLUTEN FREE<div class="badge-dots"><i></i><i></i><i></i><i class="big"></i><i></i><i></i><i></i></div></div>
    <div class="title-mint"><span class="brand-name">Hale Kin.</span><div class="product-name">POLAR FROST<br>DROPS</div></div>
    <div class="banner"><div class="banner-net"><i></i><i class="mid"></i><i class="big"></i><span>175g NET</span><i class="big"></i><i class="mid"></i><i></i></div><div class="banner-tag">A flavour for every memory!</div></div>
    <div class="contact">
      <p class="contact-brand">Hale Kin. SWEETS</p>
      <p>88 Harbour Lane<br>Level 2, Suite 410<br>CAIRNS QLD 4870<br>PO Box 19<br>KURANDA QLD 4881<br>AUSTRALIA<br>+61 (07) 4000 1234</p>
      <p class="contact-web">www.halekinsweets.com<br>AU: sales@halekinsweets.com.au<br>USA, EU, UK, Canada:<br>sales@halekinsweets.com</p>
      <p class="contact-social"><i></i>HaleKinSweets</p>
    </div>
    <div class="batch"><b>Best before:</b> Jun 2028<br><b>Batch/lot number:</b> 1400/09001-26007</div>
  </section>
</body>
</html>
```